Thoroughbred Racing Partnership needs web design

Crown of Laurels Partners is a management group who buys horses and races them on both the West and East coasts. The premise of the business is for an investment as little as $500, anyone can be a partner and own a percentage of a horse(s). This is a low cost way of getting involved in the exciting sport of Thoroughbred Racing, without shouldering the heavy financial responsibility. Our target market is mostly males 40+ but we want to include all target markets. We are looking for something very clean and professional, we want to give an image of success. Nothing overly "artsy." I have included the logo in which you can incorporate in the site. Also, the logo colors will be the colors of our "silks." The silks are what the jockey wears and will be an important marketing tool for COL. We would like a very prominent picture of a racehorse somewhere on the homepage, we want to make it clear that is a website for Horseracing partnerships.

On the top of the site, it should say "Crown of Laurels" (on the top)
and below that "Thoroughbred Racing Partnerships." (below that)

The main sections, which should be across the top are:

Home
About Us
Ownership
Stable Roster
News
Contact us

Some of these will have drop down menus.

An example of a competitor website that we like is: www.harrowfieldstable.example
An example of a competitor website that we don't like is: www.gallopmarket.example
Updates

Project Deadline Extended
Reason: We have a Board of Directors meeting on the 22nd and we will be making a decision on that day. I'm giving an extension so that all designers are able to submit their designs by the 22nd. Thank you!

Target Market(s)

40+ males

Industry/Entity Type

Business

Requirements
Must have
• our logo must be on the site. We would like at least one bold image of a thoroughbred horse in action. The picture is going to tell the story so it needs to be very eye-catching.

Our slogan should also be included on the website, "Experience the thrill of owning a Racehorse."
Should not have
• cartoons, artsy pictures, pictures of Steeplechase horses or "jumpers." This partnership is for racehorses only, there is not jumping involved with the horses.

```html
<!DOCTYPE html>
<html lang="en">
<head>
<meta charset="utf-8">
<title>Crown of Laurels Partners</title>
<link href="https://fonts.googleapis.com/css2?family=Arvo:wght@400;700&family=Open+Sans:wght@400;600;700&display=swap" rel="stylesheet">
<style>
:root{
  --navy:#1c3f6e;
  --navy-dark:#1f3a5c;
  --bar:#203a5a;
  --link:#1d5fae;
  --text:#333;
  --grey-nav:#7a7a7a;
  --footer:#9aa0a7;
  --footer-head:#6e747b;
  --footer-link:#4f555c;
  --white:#fff;
}
*{margin:0;padding:0;box-sizing:border-box}
html,body{width:1152px;height:1200px;overflow:hidden;background:var(--white)}
body{position:relative;font-family:"Open Sans",Arial,sans-serif;color:var(--text)}
.hero{position:absolute;left:0;top:0;width:1152px;height:562px;
  background:linear-gradient(180deg,#f1f2f4 0%,#e4e6ea 45%,#cfd0cf 62%,#6b4c35 80%,#4a3424 100%)}
.top-line{position:absolute;left:0;top:0;width:1152px;height:5px;background:var(--navy)}
.call-tab{position:absolute;left:696px;top:0;width:330px;height:30px;background:var(--bar);
  clip-path:polygon(0 0,100% 0,98% 100%,1% 100%);display:flex;align-items:center;justify-content:center;gap:9px;
  font-family:"Arvo",Georgia,serif;font-size:15px;color:#a9b6c8;letter-spacing:.5px}
.call-tab strong{color:var(--white);font-weight:700;letter-spacing:.3px}
.brand{position:absolute;left:125px;top:30px;color:var(--navy);font-family:"Arvo",Georgia,serif;font-weight:700;line-height:1}
.brand .big{display:block;font-size:44px;letter-spacing:4px}
.brand .small{display:block;font-size:17px;letter-spacing:1px;margin-top:6px}
.main-nav{position:absolute;top:62px;left:0}
.main-nav a{position:absolute;white-space:nowrap;font-family:"Arvo",Georgia,serif;font-size:16px;color:var(--grey-nav);text-decoration:none}
.main-nav a.active{color:var(--navy)}
.hero-copy{position:absolute;left:630px;top:170px}
.hero-copy h1{font-family:"Arvo",Georgia,serif;font-weight:400;font-size:46px;color:var(--navy);letter-spacing:.5px}
.hero-copy p{font-size:24px;color:#666;margin:10px 0 0 6px}
.btn{position:absolute;left:6px;top:117px;width:134px;height:43px;border-radius:3px;
  background:linear-gradient(#5a6e8c,#3b4f6d);border:1px solid #2e4060;color:var(--white);
  font-weight:700;font-size:15px;display:flex;align-items:center;justify-content:center;text-decoration:none}
.dots{position:absolute;left:543px;top:516px;display:flex;gap:10px}
.dots span{width:10px;height:10px;border-radius:50%;background:#a7a29c}
.dots span.on{background:var(--white)}
.features{position:absolute;top:590px;left:0}
.feature{position:absolute;top:0}
.feature h2{font-family:"Arvo",Georgia,serif;font-weight:400;font-size:25px;color:var(--navy);letter-spacing:1.5px;white-space:nowrap}
.feature .photo{margin-top:8px;height:189px}
.feature p{margin-top:28px;font-size:12px;line-height:17.3px;padding-left:3px}
.feature a{display:inline-block;margin-top:14px;margin-left:3px;font-size:12px;font-weight:700;color:var(--link)}
.site-footer{position:absolute;left:0;top:987px;width:1152px;height:166px;background:var(--footer)}
.footer-brand{position:absolute;left:187px;top:42px;color:#737980;font-family:"Arvo",Georgia,serif;font-weight:700;line-height:1}
.footer-brand .big{display:block;font-size:40px;letter-spacing:4px}
.footer-brand .small{display:block;font-size:19px;letter-spacing:5px;margin-top:6px}
.footer-col{position:absolute;top:27px;font-size:12px}
.footer-col h3{font-family:"Arvo",Georgia,serif;font-weight:400;font-size:12.5px;color:var(--footer-head);letter-spacing:1px;margin-bottom:7px}
.footer-col a,.footer-col span{display:block;line-height:23px;color:var(--footer-link);font-weight:600;text-decoration:none}
.footer-col span{font-weight:400;color:#474d54}
.bottom-bar{position:absolute;left:0;top:1153px;width:1152px;height:47px;background:var(--navy-dark);
  display:flex;align-items:center;justify-content:center;font-size:12.5px;color:#b7c0cc;letter-spacing:.3px}
</style>
</head>
<body>
<header>
  <div class="hero" role="img" aria-label="Racehorse and jockey in silks at full stretch in front of a grandstand"></div>
  <div class="top-line"></div>
  <div class="call-tab">
    <svg width="14" height="14" viewBox="0 0 24 24" fill="#7f8ea4" aria-hidden="true"><path d="M6.6 10.8a15.1 15.1 0 0 0 6.6 6.6l2.2-2.2a1 1 0 0 1 1-.25 11.4 11.4 0 0 0 3.6.57 1 1 0 0 1 1 1V20a1 1 0 0 1-1 1A17 17 0 0 1 3 4a1 1 0 0 1 1-1h3.5a1 1 0 0 1 1 1c0 1.25.2 2.45.57 3.57a1 1 0 0 1-.25 1z"/></svg>
    CALL US TODAY <strong>1800 555 0199</strong>
  </div>
  <div class="brand"><span class="big">COL</span><span class="small">PARTNERS</span></div>
  <nav class="main-nav">
    <a class="active" href="#" style="left:490px">Home</a>
    <a href="#" style="left:572px">About</a>
    <a href="#" style="left:650px">Ownership</a>
    <a href="#" style="left:763px">Stable Roster</a>
    <a href="#" style="left:898px">News</a>
    <a href="#" style="left:970px">Contact</a>
  </nav>
  <div class="hero-copy">
    <h1>Crown of Laurels.</h1>
    <p>Thoroughbred Racing Partnerships.</p>
    <a class="btn" href="#">Learn More</a>
  </div>
  <div class="dots"><span class="on"></span><span></span><span></span><span></span></div>
</header>

<main class="features">
  <section class="feature" style="left:125px;width:298px">
    <h2>ABOUT COL</h2>
    <div class="photo" role="img" aria-label="Racehorse galloping on turf" style="background:linear-gradient(160deg,#c33a3a 0%,#3d2a22 40%,#5b7a3a 75%,#d4b23a 100%)"></div>
    <p>Lorem ipsum dolor sit amet, consectetur adipisicing elit, sed do eiusmod tempor incididunt ut labore et dolore magna aliqua. Ut enim ad minim veniam, quis nostrud exercitation.</p>
    <a href="#">READ MORE</a>
  </section>
  <section class="feature" style="left:443px;width:287px">
    <h2>OWNERSHIP</h2>
    <div class="photo" role="img" aria-label="Close view of racehorses running" style="background:linear-gradient(150deg,#6b3a22 0%,#b0643a 45%,#7a3a22 75%,#3a2418 100%)"></div>
    <p>Lorem ipsum dolor sit amet, consectetur adipisicing elit, sed do eiusmod tempor incididunt ut labore et dolore magna aliqua. Ut enim ad minim veniam, quis nostrud exercitation.</p>
    <a href="#">READ MORE</a>
  </section>
  <section class="feature" style="left:750px;width:298px">
    <h2>LATEST NEWS</h2>
    <div class="photo" role="img" aria-label="Partners presenting a racing award plaque" style="background:linear-gradient(135deg,#5a6f93 0%,#2a2a2e 45%,#1c1c22 70%,#2b3a66 100%)"></div>
    <p>Lorem ipsum dolor sit amet, consectetur adipisicing elit, sed do eiusmod tempor incididunt ut labore et dolore magna aliqua. Ut enim ad minim veniam, quis nostrud exercitation.</p>
    <a href="#">READ MORE</a>
  </section>
</main>

<footer class="site-footer">
  <div class="footer-brand"><span class="big">COL</span><span class="small">PARTNERS</span></div>
  <div class="footer-col" style="left:426px">
    <h3>NAVIGATION</h3>
    <a href="#">Home</a><a href="#">Ownership</a><a href="#">Stable Roster</a>
  </div>
  <div class="footer-col" style="left:606px">
    <h3>ABOUT US</h3>
    <a href="#">About</a><a href="#">News</a><a href="#">Contact Us</a>
  </div>
  <div class="footer-col" style="left:779px">
    <h3>CONTACT US</h3>
    <span>Phone : +61 3 555 0142</span>
    <span>Email: info@colpartners.example</span>
    <span>Your Street, Your Avenue</span>
    <span>Your Country, 10001</span>
  </div>
</footer>
<div class="bottom-bar">© Copyright 2013 COL PARTNERS. All Right Reserved | Privacy Policy | Site Map</div>
</body>
</html>
```